UPDATE: I have uploaded the selected logo from the other contest, please use it in your designs.

I have a logo design contest as well so not sure how ArtHive handles that. They should integrate at some point. I will describe the overall theme with the logo description. See it for details.

The business card side of it would just build on that same theme.

Target Market(s)

8-40

Industry/Entity Type

Business

Contact Information for Business Card

FirstName LastName
Email

Logo Text

VelMarin

Font styles to use
Sans Serif

Requirements
Must have
• the url VelMarin.com somewhere in it.

```html
<!DOCTYPE html>
<html lang="en">
<head>
<meta charset="UTF-8">
<title>VelMarin Business Card – Front and Back</title>
<link href="https://fonts.googleapis.com/css2?family=Arimo:wght@400;700&family=Poppins:wght@600&display=swap" rel="stylesheet">
<style>
  :root {
    --frame-blue: #1a6db3;
    --brand-blue: #0e72bd;
    --brand-green: #8cc63f;
    --ink-grey: #555556;
    --ink-mid: #444446;
    --label-ink: #2f2f30;
    --card-dark: #353334;
    --mascot-grey: #5e5e60;
    --rule-light: #cfcfcf;
    --paper: #ffffff;
  }
  * { margin: 0; padding: 0; box-sizing: border-box; }
  html, body { width: 1200px; height: 1000px; overflow: hidden; background: var(--paper); }
  .board { position: relative; width: 1200px; height: 1000px; font-family: "Arimo", Arial, sans-serif; }
  .panel { position: absolute; left: 0; width: 1200px; height: 500px; border: 2px solid var(--frame-blue); }
  .panel--front { top: 0; }
  .panel--back { top: 500px; border-top: none; }

  .card-front { position: absolute; left: 37px; top: 30px; width: 792px; height: 448px;
    border: 1px solid #333; background: var(--paper); overflow: hidden; }
  .mascot-area { position: absolute; left: 0; top: 125px; width: 298px; height: 330px;
    border-radius: 0 60% 10% 0 / 0 45% 10% 0;
    background: radial-gradient(ellipse at 40% 45%, #7a7a7c 0%, var(--mascot-grey) 55%, #4d4d4f 100%); }
  .band-blue { position: absolute; left: 0; top: 376px; width: 792px; height: 38px; background: var(--brand-blue); }
  .band-green { position: absolute; left: 724px; top: 0; width: 39px; height: 448px; background: var(--brand-green); }
  .brand-name { position: absolute; right: 86px; top: 62px; display: flex; align-items: center; gap: 14px;
    font-weight: 700; font-size: 66px; line-height: 1; color: var(--brand-blue); letter-spacing: 2px; }
  .brand-dot { width: 22px; height: 22px; border-radius: 50%; background: var(--brand-green); }
  .contact { position: absolute; right: 88px; text-align: right; white-space: nowrap; }
  .contact--name { top: 156px; font-size: 34px; font-weight: 700; color: var(--ink-grey); }
  .contact--email { top: 214px; font-size: 26px; color: var(--ink-mid); }
  .contact--web { top: 266px; font-size: 24px; color: var(--ink-grey); }
  .contact--web b { font-weight: 700; color: var(--ink-mid); }

  .card-back { position: absolute; left: 378px; top: 13px; width: 792px; height: 452px;
    background: var(--card-dark); border: 1px solid #4a5a6a; }
  .back-mascot { position: absolute; left: 532px; top: 150px; width: 95px; height: 74px;
    border-radius: 45%; background: radial-gradient(circle, rgba(120,120,122,.55), rgba(90,90,92,.15)); }
  .back-url { position: absolute; left: 0; width: 792px; top: 188px; text-align: center;
    font-size: 40px; color: var(--rule-light); }
  .back-url b { font-weight: 700; color: var(--brand-green); }
  .back-rule { position: absolute; left: 0; top: 230px; }

  .side-label { position: absolute; font-family: "Poppins", "Century Gothic", sans-serif; font-weight: 600;
    color: var(--label-ink); transform: rotate(-20deg); line-height: 1; white-space: nowrap; }
  .side-label--front-main { left: 845px; top: 150px; font-size: 84px; }
  .side-label--front-sub { left: 1035px; top: 215px; font-size: 60px; }
  .side-label--back-main { left: 28px; top: 665px; font-size: 84px; }
  .side-label--back-sub { left: 200px; top: 735px; font-size: 60px; }
</style>
</head>
<body>
<div class="board">
  <section class="panel panel--front">
    <div class="card-front">
      <div class="mascot-area" role="img" aria-label="Large grey mascot character illustration"></div>
      <div class="band-blue"></div>
      <div class="band-green"></div>
      <div class="brand-name"><span class="brand-dot"></span>VelMarin</div>
      <p class="contact contact--name">FirstName LastName</p>
      <p class="contact contact--email">email@velmarin.com</p>
      <p class="contact contact--web">www.<b>VelMarin</b>.com</p>
    </div>
  </section>
  <div class="side-label side-label--front-main">Front</div>
  <div class="side-label side-label--front-sub">Side</div>

  <section class="panel panel--back">
    <div class="card-back">
      <div class="back-mascot" role="img" aria-label="Faint mascot character decoration"></div>
      <p class="back-url">www.<b>VelMarin</b>.com</p>
      <svg class="back-rule" width="792" height="30" viewBox="0 0 792 30" aria-hidden="true">
        <line x1="102" y1="15" x2="374" y2="15" stroke="#cfcfcf" stroke-width="3"/>
        <line x1="418" y1="15" x2="690" y2="15" stroke="#cfcfcf" stroke-width="3"/>
        <circle cx="396" cy="15" r="9" fill="#ffffff"/>
      </svg>
    </div>
  </section>
  <div class="side-label side-label--back-main">Back</div>
  <div class="side-label side-label--back-sub">Side</div>
</div>
</body>
</html>
```